Business Cards, Letterhead and Email signature for Halvern Building Collective
Halvern Building Collective
Professional
Doran Pellick
Partner
Office: 4100 Birchmont Ave Suite 900 Charlotte, NC 28211
Mailing: 5217 Birchmont Ave #482 Charlotte, NC 28211
dpellick@halvernbuildingcoll.example
halvvernbuildingcoll.example
I am open to ideas, maybe the logo with a matching background color. Be creative

```html
<!DOCTYPE html>
<html lang="en">
<head>
<meta charset="utf-8">
<title>Halvern Building Collective — Business Cards</title>
<link rel="stylesheet" href="https://fonts.googleapis.com/css2?family=Archivo:wght@400;800&display=swap">
<style>
  :root {
    --stage: #e7e5e1;
    --card-white: #ffffff;
    --card-frost: #e4e7ea;
    --brand-blue: #1c4aa6;
    --brand-blue-deep: #0b2a7c;
    --brand-blue-light: #3a6cd0;
    --silver: #c9ced6;
    --silver-light: #f4f6f9;
    --ink-blue: #1d3f8f;
    --ink-grey: #5b6470;
    --white: #ffffff;
  }
  * { margin: 0; padding: 0; box-sizing: border-box; }
  html, body { width: 1200px; height: 730px; overflow: hidden; }
  body {
    background: var(--stage);
    font-family: "Archivo", Arial, sans-serif;
    position: relative;
  }
  .card {
    position: absolute;
    width: 470px;
    height: 285px;
    border-radius: 18px;
    overflow: hidden;
    box-shadow: 0 6px 18px rgba(0,0,0,0.18);
  }
  .card--white { background: var(--card-white); }
  .card--frost { background: var(--card-frost); }
  .pos-front-white { left: 70px;  top: 60px; }
  .pos-front-frost { left: 660px; top: 60px; }
  .pos-back-white  { left: 70px;  top: 385px; }
  .pos-back-frost  { left: 660px; top: 385px; }

  .brand {
    position: absolute;
    left: 0; right: 0;
    top: 58px;
    display: flex;
    justify-content: center;
    align-items: center;
    gap: 12px;
  }
  .brand__square {
    width: 34px; height: 34px;
    background: var(--ink-blue);
  }
  .brand__name {
    font-weight: 800;
    font-size: 24px;
    letter-spacing: 0.5px;
    color: var(--ink-blue);
    text-transform: uppercase;
    line-height: 1;
  }
  .brand--mirrored { transform: scaleX(-1); opacity: 0.55; }

  .band {
    position: absolute;
    left: 0; right: 0; bottom: 0;
    height: 128px;
    background: linear-gradient(180deg, var(--brand-blue-light) 0%, var(--brand-blue) 35%, var(--brand-blue-deep) 100%);
  }
  .band::before {
    content: "";
    position: absolute;
    left: 0; right: 0; top: -6px;
    height: 6px;
    background: linear-gradient(90deg, var(--silver) 0%, var(--silver-light) 50%, var(--silver) 100%);
  }
  .card--frost .band { opacity: 0.92; }

  .person {
    position: absolute;
    left: 0; right: 0; top: 128px;
    text-align: center;
    font-size: 10px;
    letter-spacing: 1.5px;
    text-transform: uppercase;
    color: var(--ink-grey);
  }
  .person__divider { margin: 0 8px; color: var(--ink-blue); }

  .contact {
    position: absolute;
    left: 24px; right: 24px; bottom: 20px;
    color: var(--white);
    font-size: 7.2px;
    letter-spacing: 0.3px;
    line-height: 1.9;
  }
  .contact__line { white-space: nowrap; }
  .contact__sep { margin: 0 5px; opacity: 0.7; }

  .website {
    position: absolute;
    left: 0; right: 0; bottom: 32px;
    text-align: center;
    color: var(--white);
    font-size: 8px;
    letter-spacing: 3px;
    text-transform: uppercase;
  }
</style>
</head>
<body>

  <!-- Front, white stock -->
  <section class="card card--white pos-front-white">
    <div class="brand"><span class="brand__square"></span><span class="brand__name">Halvern Building Collective</span></div>
    <p class="person">Doran Pellick<span class="person__divider">|</span>Partner</p>
    <div class="band"></div>
    <div class="contact">
      <p class="contact__line">4100 Birchmont Ave Suite 900 Charlotte, NC 28211<span class="contact__sep">|</span>T 704-555-0142<span class="contact__sep">|</span>F 704-555-0143</p>
      <p class="contact__line">5217 Birchmont Ave #482 Charlotte, NC 28211<span class="contact__sep">|</span>dpellick@halvernbuildingcoll.example<span class="contact__sep">|</span>Skype Halvern4418</p>
      <p class="contact__line">C 704-555-0144</p>
    </div>
  </section>

  <!-- Front, frosted stock -->
  <section class="card card--frost pos-front-frost">
    <div class="brand"><span class="brand__square"></span><span class="brand__name">Halvern Building Collective</span></div>
    <p class="person">Doran Pellick<span class="person__divider">|</span>Partner</p>
    <div class="band"></div>
    <div class="contact">
      <p class="contact__line">4100 Birchmont Ave Suite 900 Charlotte, NC 28211<span class="contact__sep">|</span>T 704-555-0142<span class="contact__sep">|</span>F 704-555-0143</p>
      <p class="contact__line">5217 Birchmont Ave #482 Charlotte, NC 28211<span class="contact__sep">|</span>dpellick@halvernbuildingcoll.example<span class="contact__sep">|</span>Skype Halvern4418</p>
      <p class="contact__line">C 704-555-0144</p>
    </div>
  </section>

  <!-- Back, white stock -->
  <section class="card card--white pos-back-white">
    <div class="brand"><span class="brand__square"></span><span class="brand__name">Halvern Building Collective</span></div>
    <div class="band"></div>
    <p class="website">www.halvvernbuildingcoll.example</p>
  </section>

  <!-- Back, frosted stock -->
  <section class="card card--frost pos-back-frost">
    <div class="brand brand--mirrored"><span class="brand__square"></span><span class="brand__name">Halvern Building Collective</span></div>
    <div class="band"></div>
    <p class="website">www.halvvernbuildingcoll.example</p>
  </section>

</body>
</html>
```